B2B EDM Banner Design- Specialist Tech Company

We need a new top-of-email banner for our EDM campaigns for Varnel Brix (www.varnelbrix-example.com
). This banner will sit at the top of every email and must immediately signal the brand, look modern and professional, and be visually aligned with the tech/IT audience.
Size of the banner: Around 728x90 - it must fit at the top of an email blast.
Purpose of the Banner
Establish a strong, recognizable brand identity across all Varnel Brix EDMs
visually consistent with existing banners created for other brands (see reference examples provided)
Communicate Varnel Brix’s value proposition at a glance
Brand Name
Varnel Brix
Tagline (must appear in the banner)
“11,322 whitepapers from 726 companies”
Design Requirements
Style & Tone
Modern, clean, and professional
Tech-centric look and feel
High-quality, sleek, and corporate
Eye-catching but not cluttered
Should feel premium and authoritative
Layout & Composition
Full-width banner for email header
Horizontal orientation similar to the Plomtar and Quindle Staff Archive examples
Include space for the brand name/logo prominently on the left or centered
Integrate the tagline in a readable, secondary position
Optional: a subtle background texture or tech-related abstract pattern (circuitry, network nodes, gradient, etc.)
No busy imagery—should feel clean and trustworthy
Color Palette
Use colors consistent with Varnel Brix branding from www.varnelbrix-example.com
Blues, greys, blacks, and tech-style gradients preferred
Should feel consistent with a B2B IT audience
Typography
Clean, sans-serif fonts (professional/tech-aligned)
Brand name should be bold and prominent
Tagline should be smaller, but still readable on desktop and mobile
Imagery (if used)
Abstract tech shapes, network visuals, geometric patterns, or gradient overlays
Avoid photography of people
Keep imagery subtle so text remains legible
Call-to-Action Button (optional)
None required in this banner (unlike the HR examples)
Banner should remain a pure brand header
Deliverables
Final banner in PNG and JPG formats
2–3 design variations (if possible) for A/B testing
Dimensions optimized for EDM: ~600–700px wide (standard email width), proportionate height

```html
<!DOCTYPE html>
<html lang="en">
<head>
<meta charset="UTF-8">
<title>Varnel Brix – EDM Header Banner Variations</title>
<link href="https://fonts.googleapis.com/css2?family=Montserrat:wght@300;400;800&display=swap" rel="stylesheet">
<style>
  :root {
    --page-bg: #ffffff;
    --navy-edge: #233f6c;
    --blue-mid: #136fae;
    --blue-core: #0a8fcf;
    --text-white: #ffffff;
    --mark-blue: #129ad8;
    --shadow: rgba(0, 0, 0, 0.22);
  }
  * { margin: 0; padding: 0; box-sizing: border-box; }
  html, body {
    width: 1200px;
    height: 494px;
    overflow: hidden;
    background: var(--page-bg);
    font-family: "Montserrat", sans-serif;
    color: var(--text-white);
  }
  .canvas { position: relative; width: 1200px; height: 494px; }

  .banner {
    position: absolute;
    left: 87px;
    width: 1034px;
    overflow: hidden;
    box-shadow: 0 8px 7px -3px var(--shadow);
  }
  .banner--one { top: 32px; height: 127px; }
  .banner--two { top: 178px; height: 130px; }
  .banner--three { top: 337px; height: 127px; }

  .banner__backdrop {
    position: absolute;
    inset: 0;
    background:
      radial-gradient(ellipse 45% 80% at 52% 45%, rgba(10, 150, 215, 0.55), transparent 70%),
      linear-gradient(90deg, var(--navy-edge) 0%, var(--blue-mid) 35%, var(--blue-core) 52%, var(--blue-mid) 70%, var(--navy-edge) 100%);
  }

  .brand-mark {
    position: absolute;
    background: var(--mark-blue);
    border-radius: 50%;
  }
  .banner--one .brand-mark { left: 123px; top: 28px; width: 72px; height: 72px; }

  .brand-tile {
    position: absolute;
    left: 114px; top: 24px;
    width: 89px; height: 80px;
    background: var(--text-white);
    border-radius: 14px;
  }

  .lockup { position: absolute; }
  .lockup__name {
    font-weight: 800;
    line-height: 1;
    white-space: nowrap;
  }
  .lockup__sub {
    font-weight: 800;
    text-transform: uppercase;
    white-space: nowrap;
    line-height: 1;
  }

  .banner--one .lockup,
  .banner--three .lockup { left: 218px; top: 38px; width: 272px; }
  .banner--one .lockup__name,
  .banner--three .lockup__name { font-size: 37px; letter-spacing: 0.01em; }
  .banner--one .lockup__sub,
  .banner--three .lockup__sub { font-size: 11px; letter-spacing: 0.62em; margin-top: 12px; }

  .divider {
    position: absolute;
    left: 512px; top: 33px;
    width: 3px; height: 62px;
    background: var(--text-white);
  }

  .tagline-large {
    position: absolute;
    left: 541px; top: 33px;
    font-weight: 300;
    font-size: 30px;
    line-height: 27px;
    width: 400px;
  }

  .banner--two .lockup {
    left: 0; right: 0; top: 17px;
    text-align: center;
  }
  .banner--two .lockup__name { font-size: 55px; letter-spacing: 0.005em; }
  .banner--two .lockup__sub { font-size: 17px; letter-spacing: 0.78em; margin-top: 11px; padding-left: 0.78em; }
  .tagline-small {
    display: block;
    font-weight: 400;
    font-size: 15px;
    margin-top: 8px;
  }
</style>
</head>
<body>
<main class="canvas">

  <section class="banner banner--one" aria-label="Variation A: brand left, tagline right">
    <div class="banner__backdrop" role="img" aria-label="Blue tech gradient with subtle circuit-board line pattern"></div>
    <span class="brand-mark" aria-hidden="true"></span>
    <div class="lockup">
      <p class="lockup__name">VARNEL BRIX</p>
      <p class="lockup__sub">For IT Professionals</p>
    </div>
    <span class="divider" aria-hidden="true"></span>
    <p class="tagline-large">11,322 whitepapers from 726 companies</p>
  </section>

  <section class="banner banner--two" aria-label="Variation B: centred brand">
    <div class="banner__backdrop" role="img" aria-label="Blue tech gradient with subtle circuit-board line pattern"></div>
    <div class="lockup">
      <p class="lockup__name">VARNEL BRIX</p>
      <p class="lockup__sub">For IT Professionals</p>
      <span class="tagline-small">11,322 whitepapers from 726 companies</span>
    </div>
  </section>

  <section class="banner banner--three" aria-label="Variation C: tiled brand left, tagline right">
    <div class="banner__backdrop" role="img" aria-label="Blue tech gradient with subtle circuit-board line pattern and light glows"></div>
    <span class="brand-tile" aria-hidden="true"></span>
    <div class="lockup">
      <p class="lockup__name">VARNEL BRIX</p>
      <p class="lockup__sub">For IT Professionals</p>
    </div>
    <span class="divider" aria-hidden="true"></span>
    <p class="tagline-large">11,322 whitepapers from 726 companies</p>
  </section>

</main>
</body>
</html>
```